Holistic Therapy (aromatherapy, massage, reflexology, life coaching, soul healing, aura reading)

I work for myself as a holistic therapist doing: aromatherapy massage, massage, reflexology, abdominal-sacral massage, life coaching, soul healing, aura readings. I want a business card that doesn't focus on any one of these( so not just feet or a massage couch,but rather a card that creates the feeling of wholeness, healing, health and which can encompass all my therapies - e.g. green or purple are colours I like (especially green, or maybe green on back and purple on front). It's going to be called Rosa Pell Therapies. I don't want to list all my therapies on the card in case I add others later.). At some point I will create a website but in this instance I just want to get some cards printed to get 'out there' while I design my website.

Hi, thanks for all your designs. Can you find a way to include the therapies that I offer within the card, either on the front or back…the therapies I offer are: aromatherapy massage, reflexology, swedish body massage, abdominal-sacral massage, nutrition, soul healing, aura readings. (Maybe have them with a bullet point before each?) I am not sure whether they should be on the front of the card or the back or whether having them would spoil the card but it occurred to me that just having rosa pell therapies doesn't tell people what therapies I offer, hence the new idea to list them somehow…)

Target Market(s)

Mainly women (middle class probably with disposable incomes).

Industry/Entity Type

Massage

Contact Information for Business Card

Rosa Pell Therapies, Tel: 07700 900482, email: lumacrest@postvane.com, (on back of card I want: Rosalind Pell BScHons, CPWRA, RGPC.)

Requirements
Nice to have
• A logo for Rosa Pell Therapies would be good.

```html
<!DOCTYPE html>
<html lang="en">
<head>
<meta charset="utf-8">
<title>Rosa Pell Therapies – Business Card</title>
<link href="https://fonts.googleapis.com/css2?family=Encode+Sans+Semi+Condensed:wght@300;400&display=swap" rel="stylesheet">
<style>
  :root {
    --backdrop: #6dffa9;
    --card-dark: #2a2327;
    --card-light: #ececec;
    --ink-light: #ffffff;
    --ink-dark: #2a2327;
    --ink-muted: #9a9a9a;
  }
  * { margin: 0; padding: 0; box-sizing: border-box; }
  html, body {
    width: 1200px;
    height: 900px;
    overflow: hidden;
    background: var(--backdrop);
    font-family: "Encode Sans Semi Condensed", "Arial Narrow", sans-serif;
  }
  .canvas {
    position: relative;
    width: 1200px;
    height: 900px;
  }
  .card {
    position: absolute;
    top: 330px;
    width: 420px;
    height: 240px;
    box-shadow: 0 6px 18px rgba(0, 0, 0, 0.18);
  }

  /* Front */
  .card--front {
    left: 150px;
    background: var(--card-light);
    padding: 12px;
  }
  .card--front .panel {
    width: 100%;
    height: 100%;
    background: var(--card-dark);
    color: var(--ink-light);
    display: flex;
    flex-direction: column;
    align-items: center;
    justify-content: center;
  }
  .front__dot {
    width: 5px;
    height: 5px;
    border-radius: 50%;
    background: var(--ink-light);
  }
  .front__name {
    font-weight: 400;
    font-size: 30px;
    letter-spacing: 0.5px;
    margin: 8px 0;
  }
  .front__credentials {
    display: flex;
    gap: 110px;
    margin-top: 22px;
    font-size: 12px;
    font-weight: 300;
    letter-spacing: 1.5px;
  }

  /* Back */
  .card--back {
    left: 630px;
    background: var(--card-dark);
    padding: 12px;
  }
  .card--back .panel {
    position: relative;
    width: 100%;
    height: 100%;
    background: var(--card-light);
    color: var(--ink-dark);
    padding: 26px 30px;
  }
  .back__brand {
    border-left: 1.5px solid var(--ink-dark);
    padding-left: 8px;
    line-height: 1.1;
  }
  .back__name {
    font-size: 26px;
    font-weight: 400;
  }
  .back__tag {
    font-size: 15px;
    font-weight: 300;
  }
  .back__rule {
    margin-top: 22px;
    width: 84%;
    height: 1px;
    background: var(--ink-dark);
  }
  .back__contact {
    position: absolute;
    left: 30px;
    bottom: 26px;
    font-size: 12px;
    line-height: 1.6;
  }
  .back__contact dt {
    display: inline-block;
    width: 52px;
    color: var(--ink-muted);
    letter-spacing: 2px;
    font-size: 9px;
  }
  .back__contact dd { display: inline; }
  .back__contact-line {
    position: absolute;
    left: 8px;
    bottom: 20px;
    width: 1px;
    height: 34px;
    background: var(--ink-muted);
  }
</style>
</head>
<body>
<main class="canvas">
  <section class="card card--front" aria-label="Card front">
    <div class="panel">
      <span class="front__dot"></span>
      <h1 class="front__name">Rosa Pell</h1>
      <span class="front__dot"></span>
      <p class="front__credentials"><span>CPWRA</span><span>RGPC</span></p>
    </div>
  </section>

  <section class="card card--back" aria-label="Card back">
    <div class="panel">
      <div class="back__brand">
        <p class="back__name">Rosa Pell</p>
        <p class="back__tag">Therapies</p>
      </div>
      <div class="back__rule"></div>
      <span class="back__contact-line"></span>
      <dl class="back__contact">
        <div><dt>PHONE</dt><dd>07700 900482</dd></div>
        <div><dt>EMAIL</dt><dd>lumacrest@postvane.com</dd></div>
      </dl>
    </div>
  </section>
</main>
</body>
</html>
```